Tervolan Pty Ltd professional business card

A professional business card template using the colours from the supplied logo.
Clean crisp lines while, Modern while not being over the top.

Target Market(s)

Construction, commerical and industrial

Industry/Entity Type

Communications

Contact Information for Business Card

For a Communications, IT, Optical fibre installation company

Colors
37b8a4

```html
<!DOCTYPE html>
<html lang="en">
<head>
<meta charset="utf-8">
<title>Tervolan Pty Ltd – Business Card</title>
<link rel="stylesheet" href="https://fonts.googleapis.com/css2?family=Lato:wght@400;700&display=swap">
<style>
  :root {
    --teal: #1fa9b8;
    --teal-deep: #158f9c;
    --grey: #6d6e72;
    --grey-light: #8a8b8f;
    --charcoal: #252325;
    --paper: #ffffff;
    --backdrop: #e9e7e3;
  }
  * { box-sizing: border-box; margin: 0; padding: 0; }
  html, body { width: 1200px; height: 903px; overflow: hidden; }
  body {
    background: var(--backdrop);
    font-family: "Lato", sans-serif;
    position: relative;
  }
  .card {
    position: absolute;
    width: 520px;
    height: 297px;
    border-radius: 18px;
    overflow: hidden;
    box-shadow: 0 10px 28px rgba(0,0,0,0.18);
  }
  .card-front { left: 70px; top: 110px; background: var(--paper); }
  .card-back { left: 610px; top: 496px; background: var(--charcoal); }
  .card-art { position: absolute; inset: 0; width: 100%; height: 100%; }

  .wordmark {
    display: flex;
    align-items: center;
    gap: 10px;
    font-weight: 700;
    letter-spacing: 3px;
    color: var(--grey);
  }
  .wordmark-dot {
    width: 14px; height: 14px; border-radius: 50%;
    background: var(--teal);
    flex: none;
  }
  .card-front .wordmark { position: absolute; top: 34px; right: 34px; font-size: 30px; }
  .card-back .wordmark { font-size: 46px; color: var(--grey-light); }

  .person { position: absolute; left: 36px; top: 82px; }
  .person-name { color: var(--teal); font-size: 24px; letter-spacing: 0.5px; line-height: 1.2; }
  .person-role { color: var(--grey); font-size: 16px; margin-top: 2px; letter-spacing: 0.5px; }

  .contact { position: absolute; left: 36px; top: 150px; color: var(--grey); font-size: 13px; letter-spacing: 0.4px; }
  .contact-address { line-height: 1.5; margin-bottom: 6px; }
  .contact-list { list-style: none; }
  .contact-list li { display: flex; align-items: center; gap: 8px; height: 20px; }
  .contact-icon { width: 15px; height: 15px; flex: none; }

  .back-brand {
    position: absolute; left: 0; right: 0; top: 88px;
    display: flex; flex-direction: column; align-items: center; gap: 8px;
  }
  .back-url { color: var(--teal); font-size: 15px; letter-spacing: 0.8px; }
</style>
</head>
<body>

<section class="card card-front" aria-label="Card front">
  <svg class="card-art" viewBox="0 0 520 297" preserveAspectRatio="none" aria-hidden="true">
    <path d="M0,287 L360,250 Q440,238 520,214 L520,297 L0,297 Z" fill="var(--teal)"/>
    <path d="M382,297 Q418,218 520,188 L520,297 Z" fill="var(--grey)"/>
    <path d="M370,297 Q406,212 520,180" fill="none" stroke="var(--paper)" stroke-width="4"/>
  </svg>

  <div class="wordmark"><span class="wordmark-dot"></span>TERVOLAN</div>

  <div class="person">
    <p class="person-name">Marcus Hale</p>
    <p class="person-role">Director</p>
  </div>

  <div class="contact">
    <p class="contact-address">1023 Street Here, Suite 123<br>City Name, State 1234</p>
    <ul class="contact-list">
      <li>
        <svg class="contact-icon" viewBox="0 0 16 16" aria-hidden="true"><circle cx="8" cy="8" r="7" fill="none" stroke="var(--teal)" stroke-width="1.3"/><path d="M5.5,4.5 L7,4.5 L7.5,6.5 L6.6,7.2 Q7.5,9 8.8,9.4 L9.5,8.5 L11.5,9 L11.5,10.5 Q8,11.5 5.5,7 Z" fill="var(--teal)"/></svg>
        012.1234 567
      </li>
      <li>
        <svg class="contact-icon" viewBox="0 0 16 16" aria-hidden="true"><circle cx="8" cy="8" r="7" fill="none" stroke="var(--teal)" stroke-width="1.3"/><rect x="4.3" y="5.5" width="7.4" height="5" fill="none" stroke="var(--teal)" stroke-width="1.1"/><path d="M4.3,5.5 L8,8.5 L11.7,5.5" fill="none" stroke="var(--teal)" stroke-width="1.1"/></svg>
        info@yourdomain.com
      </li>
      <li>
        <svg class="contact-icon" viewBox="0 0 16 16" aria-hidden="true"><circle cx="8" cy="8" r="7" fill="none" stroke="var(--teal)" stroke-width="1.2"/><ellipse cx="8" cy="8" rx="3" ry="7" fill="none" stroke="var(--teal)" stroke-width="1"/><path d="M1,8 H15 M2,4.5 H14 M2,11.5 H14" stroke="var(--teal)" stroke-width="1"/></svg>
        www.yourdomain.com
      </li>
    </ul>
  </div>
</section>

<section class="card card-back" aria-label="Card back">
  <svg class="card-art" viewBox="0 0 520 297" preserveAspectRatio="none" aria-hidden="true">
    <path d="M0,262 Q130,238 250,258 L520,212 L520,232 L0,297 Z" fill="var(--teal)"/>
    <path d="M0,270 Q140,248 262,268 L0,297 Z" fill="var(--grey)"/>
    <path d="M0,266 Q140,243 262,266" fill="none" stroke="var(--charcoal)" stroke-width="3"/>
  </svg>

  <div class="back-brand">
    <div class="wordmark"><span class="wordmark-dot"></span>TERVOLAN</div>
    <p class="back-url">www.yourdomain.com</p>
  </div>
</section>

</body>
</html>
```